Conference flyer

We need a flyer for a conference for the defence industry. The attached has been updated with new information using last years flyer. We would like something new and fresh. Please note the theme of the conference is 'a global environment'.

The final design should reflect the defence industry and manufacturing.

Defence

```html
<!DOCTYPE html>
<html lang="en">
<head>
<meta charset="utf-8">
<title>Allied Trade Compliance – Annual Conference Flyer</title>
<link rel="stylesheet" href="https://fonts.googleapis.com/css2?family=Roboto+Condensed:ital,wght@0,400;0,700;1,400;1,700&display=swap">
<style>
:root{
  --blue:#1f6fb5;
  --blue-dark:#0d4a86;
  --blue-light:#d6e4f2;
  --paper:#f1f1ee;
  --ink:#2f3338;
  --muted:#6b7178;
  --rule:#b9c2cb;
  --stage:#e3e6e9;
}
*{box-sizing:border-box;margin:0;padding:0}
html,body{width:1200px;height:800px;overflow:hidden}
body{background:var(--stage);font-family:"Roboto Condensed",Arial,sans-serif;color:var(--ink);
  display:flex;align-items:center;justify-content:center;gap:20px}
.spread{display:flex;box-shadow:0 6px 18px rgba(0,0,0,.18)}
.page{width:285px;height:403px;background:var(--paper);position:relative;overflow:hidden;display:flex;flex-direction:column}
.spread .page+.page{border-left:1px solid #d4d6d6}
.page-head{background:linear-gradient(100deg,var(--blue-dark) 0%,var(--blue) 70%,#4f93cf 100%);color:#fff;padding:8px 12px 7px}
.page-head .title{font-weight:700;font-size:15px;letter-spacing:.3px;line-height:1}
.page-head .sub{font-size:8px;letter-spacing:.8px;text-transform:uppercase;margin-top:2px;opacity:.9}
.page-foot{position:absolute;left:0;right:0;bottom:0;height:6px;background:var(--blue)}
.body{padding:9px 12px 14px;flex:1;font-size:5.8px;line-height:1.45}
h2{color:var(--blue);font-weight:700;font-size:11px;text-transform:uppercase;line-height:1.05}
h3{color:var(--blue);font-weight:700;font-size:7px;text-transform:uppercase;margin:5px 0 2px}
.dayline{font-weight:700;font-size:6.4px;text-transform:uppercase;color:var(--ink);margin-bottom:3px}
.cols{display:flex;gap:10px}
.cols>div{flex:1;min-width:0}
.sched li{list-style:none;display:flex;gap:4px}
.sched b{color:var(--blue-dark);min-width:18px}
.band{background:var(--blue-light);color:var(--blue);font-weight:700;font-size:9px;text-transform:uppercase;padding:4px 12px;margin:8px -12px 6px}
.price-row{display:flex;justify-content:space-between;border-bottom:1px solid var(--rule);padding:2px 0}
.price-row strong{color:var(--blue-dark)}
.info p{margin-bottom:3px}
.info strong{color:var(--blue-dark)}
.contact-row{display:flex;justify-content:space-between;margin:6px 0 8px}
.contact{display:flex;align-items:center;gap:4px}
.contact svg{width:16px;height:16px;flex:none}
.contact .lbl{font-weight:700;color:var(--blue);font-size:7px;text-transform:uppercase;line-height:1}
.field{display:flex;align-items:flex-end;gap:3px;height:10px}
.field span{white-space:nowrap}
.field i{flex:1;border-bottom:1px solid var(--rule)}
.checks{display:flex;gap:8px;margin-top:3px}
.checks span::before{content:"";display:inline-block;width:5px;height:5px;border:1px solid var(--muted);margin-right:2px;vertical-align:-1px}
.office{margin-top:8px;display:flex;gap:6px;align-items:stretch}
.office .tag{background:var(--blue);color:#fff;font-weight:700;font-size:7px;padding:4px 6px;text-transform:uppercase;line-height:1.1}
.office .lines{flex:1}
.cover-intro{font-size:6.6px;color:var(--ink);text-align:right;line-height:1.35}
.cover-theme{font-style:italic;font-weight:700;color:var(--blue);font-size:9px;text-align:right;margin:3px 0 6px}
.cover-when{margin-top:40px;width:140px;position:relative;z-index:1}
.cover-date{color:var(--blue);font-weight:700;font-size:16px;line-height:1}
.cover-venue{font-weight:700;font-size:12px;color:var(--ink);line-height:1.1;margin-top:2px}
.cover-art{position:absolute;right:0;top:96px;width:128px;height:110px;
  background:radial-gradient(circle at 60% 55%,#c9d6e0 0%,#9cb2c3 35%,#e3e9ee 70%,var(--paper) 100%)}
.speakers{margin-top:6px}
.speakers li{list-style:none;font-size:5.9px;text-align:right}
.speakers b{color:var(--blue-dark)}
.more{color:var(--blue);font-weight:700;font-style:italic;text-align:right;font-size:6.5px;margin-top:2px}
.partners{position:absolute;left:12px;right:12px;bottom:14px;display:flex;justify-content:space-between;align-items:center}
.partner{display:flex;align-items:center;gap:3px;font-size:6.5px;font-weight:700;color:var(--blue-dark)}
.partner .dot{width:8px;height:8px;border-radius:50%;background:var(--blue)}
.partner .square{width:8px;height:8px;background:var(--blue)}
</style>
</head>
<body>

<section class="spread inside">
  <article class="page program">
    <header class="page-head"><div class="title">ALLIED TRADE COMPLIANCE</div><div class="sub">Annual Conference</div></header>
    <div class="body">
      <div class="cols">
        <div>
          <h2>Day 1</h2>
          <div class="dayline">Tuesday 2 June 2015:</div>
          <ul class="sched">
            <li><b>08:30</b>Registration &amp; welcome coffee</li>
            <li><b>09:00</b>Opening address</li>
            <li><b>09:15</b>Keynote: global controls outlook</li>
            <li><b>10:00</b>Export permits in practice</li>
            <li><b>10:45</b>Morning tea</li>
            <li><b>11:15</b>Brokering and re-export rules</li>
            <li><b>12:30</b>Lunch</li>
            <li><b>13:30</b>Compliance reform panel</li>
            <li><b>14:30</b>Case study: supply chains</li>
            <li><b>15:15</b>Afternoon tea</li>
            <li><b>15:45</b>Industry question panel</li>
            <li><b>16:45</b>Close &amp; networking drinks</li>
          </ul>
        </div>
        <div>
          <h2>Day 2</h2>
          <div class="dayline">Wednesday 3 June 2015</div>
          <ul class="sched">
            <li><b>08:30</b>Day two welcome</li>
            <li><b>09:00</b>Licensing and agreements</li>
            <li><b>09:45</b>Managing technical data</li>
            <li><b>10:30</b>Morning tea</li>
            <li><b>11:00</b>The good, the bad and the audit</li>
            <li><b>12:15</b>Lunch</li>
            <li><b>13:15</b>European Union update</li>
            <li><b>14:00</b>Treaty changes explained</li>
            <li><b>14:45</b>Afternoon tea</li>
            <li><b>15:15</b>Open forum and wrap up</li>
            <li><b>16:00</b>Conference close</li>
          </ul>
        </div>
      </div>
      <div class="band">4 x half day pre and post training sessions</div>
      <h3>Pre conference training modules:</h3>
      <p><strong>Monday 1 June: Module 1</strong> – trade controls for beginners</p>
      <p><strong>Monday 1 June: Module 2</strong> – practical management of export controls</p>
      <h3>Post conference training modules:</h3>
      <p><strong>Thursday 4 June: Module 3</strong> – tips and tricks for best practice</p>
      <p><strong>Thursday 4 June: Module 4</strong> – helping beginners make the best of the conference</p>
    </div>
    <div class="page-foot"></div>
  </article>

  <article class="page info">
    <header class="page-head"><div class="title">ALLIED TRADE COMPLIANCE</div><div class="sub">Annual Conference</div></header>
    <div class="body">
      <h2>Conference prices</h2>
      <div class="dayline">All prices include GST</div>
      <div class="price-row"><span><strong>Super Earlybird</strong> (before 31 March 2015)</span><strong>$1,250</strong></div>
      <div class="price-row"><span><strong>Earlybird</strong> (before 30 April 2015)</span><strong>$1,450</strong></div>
      <div class="price-row"><span><strong>Standard</strong> (after 30 April 2015)</span><strong>$1,650</strong></div>
      <div class="price-row"><span><strong>Half day module</strong> (each)</span><strong>$395</strong></div>
      <div class="band">General information</div>
      <h3>Conference venue:</h3>
      <p><strong>Harbourview Centre Melbourne</strong><br>8 Wharf Road, Southbank VIC 3006<br>PH: (03) 9000 1234</p>
      <div class="info" style="margin-top:5px">
        <p><strong>Registration fee includes:</strong> all sessions, conference papers, lunches, teas and networking drinks.</p>
        <p><strong>Dress code:</strong> business attire for both conference days.</p>
        <p><strong>Group discounts:</strong> register three or more attendees and save ten per cent.</p>
        <p><strong>Early bird offers:</strong> payment must be received by the stated date to qualify.</p>
        <p><strong>Cancellation fee:</strong> a fee of $250 applies to all cancellations. Refunds are not available within 14 days of the event; a replacement attendee is welcome.</p>
        <p><strong>Payment terms:</strong> payment must be made prior to the event or admission will not be permitted. Electronic tickets are issued on registration and must be presented upon entry.</p>
      </div>
    </div>
    <div class="page-foot"></div>
  </article>
</section>

<section class="spread outside">
  <article class="page register">
    <header class="page-head"><div class="title">ALLIED TRADE COMPLIANCE</div><div class="sub">Annual Conference</div></header>
    <div class="body">
      <h2>How to register</h2>
      <div class="dayline">Complete the registration form below and return it to us by:</div>
      <div class="contact-row">
        <div class="contact">
          <svg viewBox="0 0 20 20"><circle cx="10" cy="10" r="8" fill="none" stroke="#1f6fb5" stroke-width="1.6"/><ellipse cx="10" cy="10" rx="3.5" ry="8" fill="none" stroke="#1f6fb5" stroke-width="1.2"/><line x1="2" y1="10" x2="18" y2="10" stroke="#1f6fb5" stroke-width="1.2"/></svg>
          <div><div class="lbl">Web</div>www.tradecontrolsforum.org.au</div>
        </div>
        <div class="contact">
          <svg viewBox="0 0 20 20"><path d="M5 2l3 4-2 2c1 2.5 3.5 5 6 6l2-2 4 3-2 3C9 18 2 11 2 5z" fill="#1f6fb5"/></svg>
          <div><div class="lbl">Phone</div>(03) 9000 1234</div>
        </div>
        <div class="contact">
          <svg viewBox="0 0 20 20"><rect x="5" y="2" width="10" height="6" fill="none" stroke="#1f6fb5" stroke-width="1.4"/><rect x="2" y="8" width="16" height="7" rx="1" fill="#1f6fb5"/><rect x="5" y="13" width="10" height="5" fill="#fff" stroke="#1f6fb5" stroke-width="1.2"/></svg>
          <div><div class="lbl">Fax</div>(03) 9000 5678</div>
        </div>
      </div>
      <div class="cols">
        <div>
          <h3>Conference registration:</h3>
          <div class="field"><span>Attendee #1</span><i></i></div>
          <div class="field"><span>Attendee #2</span><i></i></div>
          <div class="field"><span>Attendee #3</span><i></i></div>
          <div class="field"><span>Attendee #4</span><i></i></div>
          <div class="field"><span>Company</span><i></i></div>
          <div class="field"><span>Address</span><i></i></div>
          <div class="field"><span>Contact no.</span><i></i></div>
          <div class="field"><span>Email</span><i></i></div>
          <div class="field"><span>Dietary needs</span><i></i></div>
          <div class="field"><span>Payment method</span><i></i></div>
          <div class="checks"><span>Credit</span><span>Debit</span><span>Charge</span></div>
          <div class="field"><span>Card name</span><i></i></div>
          <div class="field"><span>Card number</span><i></i></div>
          <div class="field"><span>Expiry</span><i></i></div>
          <div class="field"><span>Signature</span><i></i></div>
        </div>
        <div>
          <h3>1/2 day training module/s:</h3>
          <p><strong>1 June 2015</strong><br>Module 1 – trade controls for beginners</p>
          <p>Module 2 – practical management of export controls</p>
          <p style="margin-top:3px"><strong>4 June 2015</strong><br>Module 3 – tips and tricks for best practice</p>
          <p>Module 4 – making the best of the conference</p>
          <h3>Training registration:</h3>
          <p>Attendee #1: Module 1 2 3 4<br>Attendee #2: Module 1 2 3 4<br>Attendee #3: Module 1 2 3 4<br>Attendee #4: Module 1 2 3 4</p>
          <p style="margin-top:3px;color:var(--blue)">Please tick which module each attendee would like to register for.</p>
        </div>
      </div>
      <div class="office">
        <div class="tag">Office<br>use only</div>
        <div class="lines">
          <div class="field"><span>Confirmation sent</span><i></i><span>Contact person</span><i></i></div>
          <div class="field"><span>Invoice no.</span><i></i><span>Paid</span><i></i></div>
        </div>
      </div>
    </div>
    <div class="page-foot"></div>
  </article>

  <article class="page cover">
    <header class="page-head" style="text-align:right"><div class="title">ALLIED TRADE COMPLIANCE</div><div class="sub">Annual Conference</div></header>
    <div class="cover-art" role="img" aria-label="Photograph of a silver globe built from jigsaw puzzle pieces, with loose pieces scattered beside it"></div>
    <div class="body" style="position:relative">
      <p class="cover-intro">Presenting the ATC 2015 Conference<br>the annual defence industry<br>global trade controls conference</p>
      <p class="cover-theme">“Trade controls in a global environment”</p>
      <div class="cover-when">
        <div class="cover-date">2 &amp; 3 JUNE, 2015</div>
        <div class="cover-venue">HARBOURVIEW CENTRE<br>MELBOURNE</div>
      </div>
      <h2 style="text-align:right;margin-top:42px;font-size:12px">Featuring presentations from:</h2>
      <ul class="speakers">
        <li><b>Helena Marsh</b> Assistant Secretary, Export Permits Directorate</li>
        <li><b>Dominic Reyes</b> Director, Export Compliance, Allied Sales Office</li>
        <li><b>Carla Halden</b> Managing Director, Halden Trade Advisors LLC</li>
        <li><b>Owen Pritchard</b> Trade Compliance Manager, Veltrana Australia</li>
        <li><b>Sam Okafor</b> Global Trade Compliance Lead, Arden Systems</li>
        <li><b>Lewis Tanner</b> Partner, Tanner &amp; Wise Lawyers</li>
        <li><b>Priya Raman</b> Director, Global Trade, Corvane Systems Corporation</li>
        <li><b>Felix Brennan</b> Director, Meridian Freight Company Ltd</li>
      </ul>
      <p class="more">...plus many more.</p>
    </div>
    <div class="partners">
      <span class="partner"><span class="dot"></span>Southern Defence Network</span>
      <span class="partner">Veltrana</span>
      <span class="partner"><span class="dot"></span>Trade Export Council</span>
      <span class="partner"><span class="square"></span></span>
    </div>
    <div class="page-foot"></div>
  </article>
</section>

</body>
</html>
```